Letterhead Design Project

Consulting Company , we want a letterhead incorporating both the picture provided and the logo provided. The font name is monotype corsiva.
Target Market(s)
Dentist
Industry/Entity Type
Consulting
Font styles to use
Other font styles liked:
- monotype corsiva

Colors
0455a3
Requirements
Must have
- the logo, the picture (see attached), the website name, the email. and the phone numbers.
- Website: www.trquillarisadvisory.solutions
- Email: will be provided to the winner, please use placeholder
- Phone numbers:
- Petra Hallum 5829017763
- Owen Vrastik 6148250397

Nice to have
- a swoop or wave across the bottom. a line up the side. I don't know guys. design something unique and professional.

Should not have
- arrows pointing off the logo or anywhere. no arrows. our logo altered in anyway. no broken circles. no variences in blue. we like our logo the way it is. the font is monotype corsiva

```html
<!DOCTYPE html>
<html lang="en">
<head>
<meta charset="utf-8">
<title>Trquillaris Advisory Letterhead</title>
<link rel="stylesheet" href="https://fonts.googleapis.com/css2?family=Cormorant+Garamond:ital,wght@0,500;1,500;1,600&display=swap">
<style>
  :root {
    --brand-blue: #2258ab;
    --wave-blue: #5a78c4;
    --wave-pale: #dfe6f5;
    --ink-grey: #6b6b6b;
    --backdrop: #959a9b;
    --paper: #ffffff;
  }
  * { margin: 0; padding: 0; box-sizing: border-box; }
  html, body { width: 1200px; height: 1200px; overflow: hidden; }
  body {
    background: var(--backdrop);
    font-family: "Cormorant Garamond", "Times New Roman", serif;
  }
  .letterhead {
    position: absolute;
    left: 136px;
    top: 0;
    width: 927px;
    height: 1200px;
    background: var(--paper);
    overflow: hidden;
  }
  .brand {
    position: absolute;
    left: 406px;
    top: 62px;
    display: flex;
    align-items: center;
    gap: 12px;
  }
  .brand-circle {
    width: 106px;
    height: 106px;
    border: 4px solid var(--brand-blue);
    border-radius: 50%;
    flex: none;
  }
  .brand-text { padding-top: 22px; }
  .brand-name {
    font-size: 27px;
    font-weight: 500;
    color: var(--ink-grey);
    line-height: 1;
    white-space: nowrap;
  }
  .brand-address {
    margin-top: 6px;
    font-style: italic;
    font-weight: 600;
    font-size: 11.5px;
    letter-spacing: 1.2px;
    color: var(--ink-grey);
    white-space: nowrap;
  }
  .wave {
    position: absolute;
    left: 0;
    top: 1040px;
    width: 927px;
    height: 104px;
  }
  .portrait {
    position: absolute;
    left: 786px;
    top: 1016px;
    width: 141px;
    height: 127px;
    background: linear-gradient(180deg, #d9d9d9 0%, #8c8c8c 55%, #2e2e2e 100%);
    border-radius: 60px 60px 0 0;
  }
  .footer-rule {
    position: absolute;
    left: 0;
    top: 1142px;
    width: 927px;
    height: 3px;
    background: var(--brand-blue);
  }
  .footer-band {
    position: absolute;
    left: 0;
    top: 1148px;
    width: 927px;
    height: 52px;
    background: var(--brand-blue);
    color: #fff;
    display: flex;
    align-items: center;
    padding: 0 22px 0 31px;
    gap: 10px;
    font-style: italic;
    font-weight: 600;
    white-space: nowrap;
  }
  .footer-web { font-size: 20px; }
  .footer-email, .footer-phone { font-size: 13px; }
  .footer-phone { display: flex; align-items: center; gap: 2px; }
  .phone-icon { width: 11px; height: 11px; }
</style>
</head>
<body>
  <main class="letterhead">
    <header class="brand">
      <div class="brand-circle"></div>
      <div class="brand-text">
        <p class="brand-name">Trquillaris Advisory, LLC</p>
        <p class="brand-address">418 Larkfield Lane, Oakmere Falls, Vermont 05861</p>
      </div>
    </header>

    <svg class="wave" viewBox="0 0 927 104" role="img" aria-label="Decorative blue line-mesh wave sweeping across the bottom of the page">
      <defs>
        <linearGradient id="waveFade" x1="0" y1="0" x2="1" y2="0">
          <stop offset="0" stop-color="var(--wave-blue)" stop-opacity="0.7"/>
          <stop offset="0.6" stop-color="var(--wave-blue)" stop-opacity="0.45"/>
          <stop offset="1" stop-color="var(--wave-pale)" stop-opacity="0.3"/>
        </linearGradient>
      </defs>
      <path d="M0 0 C180 40 260 60 420 50 C600 38 760 5 927 10 L927 104 L0 104 Z" fill="url(#waveFade)"/>
    </svg>

    <div class="portrait" role="img" aria-label="Black and white portrait photograph of a consultant"></div>

    <div class="footer-rule"></div>
    <footer class="footer-band">
      <span class="footer-web">www.trquillarisadvisory.solutions</span>
      <span class="footer-email">Email: name@trquillarisadvisory.solutions</span>
      <span class="footer-phone">
        <svg class="phone-icon" viewBox="0 0 24 24"><path fill="#fff" d="M6.6 10.8a15 15 0 0 0 6.6 6.6l2.2-2.2c.3-.3.7-.4 1-.2 1.1.4 2.3.6 3.6.6.6 0 1 .4 1 1V20c0 .6-.4 1-1 1A17 17 0 0 1 3 4c0-.6.4-1 1-1h3.5c.6 0 1 .4 1 1 0 1.3.2 2.5.6 3.6.1.3 0 .7-.2 1z"/></svg>
        Petra Hallum 5829017763
      </span>
      <span class="footer-phone">
        <svg class="phone-icon" viewBox="0 0 24 24"><path fill="#fff" d="M6.6 10.8a15 15 0 0 0 6.6 6.6l2.2-2.2c.3-.3.7-.4 1-.2 1.1.4 2.3.6 3.6.6.6 0 1 .4 1 1V20c0 .6-.4 1-1 1A17 17 0 0 1 3 4c0-.6.4-1 1-1h3.5c.6 0 1 .4 1 1 0 1.3.2 2.5.6 3.6.1.3 0 .7-.2 1z"/></svg>
        Owen Vrastik 6148250397
      </span>
    </footer>
  </main>
</body>
</html>
```